依頼詳細
ロゴはミナモワークスで作成していただいていますので、それを使用していただいきたいです。ホームページは現在作成中です。ロゴを取り入れ、柔らかい雰囲気でシンプルなイメージ、わかりやすい感じがいいです。
記載項目
病院名、ロゴ、開業日、内覧会の日程、住所、電話番号、ホームページのアドレス、診察時間、休診日 対象動物、挨拶等
サイズ
A4
ページ数
片面
希望イメージ
シンプル 複雑
単色 カラフル
暗い 明るい
日常 高級
遊び心 厳粛
未来的 伝統的
女性的 男性的
希望する色
納品ファイル
補足説明
ロゴを添付します。

挨拶内容
「はじめまして、はるかぜペットクリニック院長の森岡健司です。大学卒業後、熊本市内の動物病院で7年間勤務し、2014年3月24日に動物病院を開院することになりました。
ホームドクターとして地域の皆様に親しまれる病院であるとともに、飼い主様と一緒に家族である動物たちの最善のケアができるように努めてまいりたいと思います。ワンちゃん達が遊べるスペースも少しですが用意してあります。ぜひ気軽に遊びにいらしてください。今後ともよろしくお願い致します。」
おそくなりましたが、ホームページのドメイン決まりました。
http://harukaze-petclinic.exampleです。
よろしくお願いいたします。
■ 選んだ理由

シンプルで開院ということがわかりやすかったため。
犬の写真の雰囲気も良かったです。

■ 提案者全員のお礼・コメント

いいデザインを多数いただいてありがとうございます。それぞれおもしろくけっこう悩ませていただきました。また、よろしくお願いいたします。

```html
<!DOCTYPE html>
<html lang="ja">
<head>
<meta charset="utf-8">
<title>はるかぜペットクリニック 開院のお知らせ</title>
<link href="https://fonts.googleapis.com/css2?family=M+PLUS+Rounded+1c:wght@400;700;800&family=Roboto+Condensed:wght@400;700&display=swap" rel="stylesheet">
<style>
:root{
  --blue:#1f78c8;
  --blue-pale:#dcebf8;
  --yellow:#ffe400;
  --orange:#f08a1c;
  --cream:#fff7d2;
  --ink:#333;
  --map:#9a9a9a;
}
*{box-sizing:border-box;margin:0;padding:0}
html,body{width:847px;height:1200px;overflow:hidden;background:#fff}
body{font-family:"M PLUS Rounded 1c",sans-serif;color:var(--ink)}
.flyer{position:relative;width:847px;height:1200px;background:#fff}

.brand{position:absolute;top:40px;left:0;width:847px;text-align:center}
.brand-dot{width:210px;height:210px;border-radius:50%;background:var(--blue);margin:0 auto 34px}
.brand-name{font-size:44px;font-weight:800;color:var(--blue);letter-spacing:1px}
.brand-en{font-size:22px;font-weight:700;color:var(--blue);margin-top:4px}

.opening-band{position:absolute;top:398px;left:28px;width:819px;height:168px;background:var(--blue)}
.open-date{position:absolute;left:228px;top:22px;color:#fff;font-family:"Roboto Condensed",sans-serif;font-size:50px;font-weight:400}
.open-title{position:absolute;left:226px;top:70px;color:var(--yellow);font-family:"Roboto Condensed",sans-serif;font-size:96px;font-weight:400;line-height:1}

.preview{position:absolute;left:12px;top:345px;width:178px;height:230px;border-radius:50%;background:var(--yellow);text-align:center}
.preview-tag{position:absolute;left:20px;top:22px;width:118px;height:54px;background:var(--orange);color:#fff;font-size:28px;font-weight:800;line-height:54px;border-radius:4px}
.preview-days{position:absolute;top:96px;left:0;width:178px;color:var(--blue);font-size:24px;font-weight:800;line-height:1.2}
.preview-days small{display:block;font-size:18px;font-weight:700;margin-top:4px}

.hours{position:absolute;left:28px;top:605px;width:285px;height:330px;background:var(--cream);padding:18px 16px;font-size:18px;line-height:1.55}
.hours-title{color:var(--blue);font-weight:800;font-size:22px;margin-bottom:6px}
.hours-title::before{content:"";display:inline-block;width:14px;height:14px;border-radius:50%;background:var(--orange);margin-right:8px}
.hours-row{display:flex}
.hours-row .day{width:100px}
.hours .late{color:var(--orange)}
.animals-title{color:var(--orange);font-weight:800;margin-top:10px}
.animals{color:var(--orange);font-weight:700}

.greeting{position:absolute;left:340px;top:618px;width:480px}
.greeting-tab{display:inline-block;background:var(--blue);color:#fff;font-size:21px;font-weight:800;padding:4px 18px;border-radius:0 0 14px 0}
.greeting p{font-size:15.5px;line-height:1.75;margin-top:12px}

.footer{position:absolute;left:0;top:962px;width:847px;height:238px;background:var(--blue-pale)}
.map{position:absolute;left:28px;top:14px;width:285px;height:210px;background:var(--map);color:#fff;font-size:18px;display:flex;align-items:center;justify-content:center}
.contact{position:absolute;left:340px;top:12px;width:480px}
.contact-head{display:flex;align-items:center;gap:14px}
.contact-dot{width:60px;height:60px;border-radius:50%;background:var(--blue)}
.contact-name{font-size:32px;font-weight:800;color:var(--blue)}
.contact-addr{font-size:15px;margin:2px 0 0 74px}
.contact-pill{display:inline-block;margin:8px 0 0 74px;background:var(--blue);color:#fff;font-size:17px;font-weight:700;padding:2px 26px;border-radius:16px}
.contact-tel{font-size:40px;font-weight:800;color:var(--blue);margin-left:74px;line-height:1.15}
.contact-line{font-size:18px;margin-left:74px;line-height:1.35}
</style>
</head>
<body>
<main class="flyer">
  <header class="brand">
    <div class="brand-dot"></div>
    <div class="brand-name">はるかぜペットクリニック</div>
    <div class="brand-en">Harukaze Pet Clinic</div>
  </header>

  <section class="opening-band">
    <div class="open-date">2014.3.24(月)</div>
    <div class="open-title">NEW OPEN!</div>
  </section>

  <div class="preview">
    <div class="preview-tag">内覧会</div>
    <div class="preview-days">3.21(金)<br>22(土)<small>10:00〜17:00</small></div>
  </div>

  <section class="hours">
    <div class="hours-title">診療時間</div>
    <div class="hours-row"><span class="day">月〜金…</span><span>9:00〜12:00</span></div>
    <div class="hours-row"><span class="day"></span><span>15:00〜19:00</span></div>
    <div class="hours-row"><span class="day">土…</span><span>9:00〜12:00</span></div>
    <div class="hours-row"><span class="day"></span><span>15:00〜<span class="late">18:00</span></span></div>
    <div>※日、祝　休診</div>
    <div class="animals-title">対象動物</div>
    <div class="animals">犬、猫、ウサギ、ハムスター等</div>
  </section>

  <section class="greeting">
    <span class="greeting-tab">ご挨拶</span>
    <p>はじめまして、はるかぜペットクリニック院長の森岡健司です。<br>大学卒業後、熊本市内の動物病院で7年間勤務し、2014年3月24日に動物病院を開院することになりました。<br>ホームドクターとして地域の皆様に親しまれる病院であるとともに、飼い主様と一緒に家族である動物たちの最善のケアができるように努めてまいりたいと思います。<br>ワンちゃん達が遊べるスペースも少しですが用意してあります。ぜひ気軽に遊びにいらしてください。<br>今後ともよろしくお願い致します。</p>
  </section>

  <footer class="footer">
    <div class="map" role="img" aria-label="クリニック周辺の地図">MAP</div>
    <div class="contact">
      <div class="contact-head"><div class="contact-dot"></div><div class="contact-name">はるかぜペットクリニック</div></div>
      <div class="contact-addr">熊本市東区さくら台２丁目8-45</div>
      <div class="contact-pill">お問い合わせ</div>
      <div class="contact-tel">TEL 096-000-4821</div>
      <div class="contact-line">FAX 096-000-4822</div>
      <div class="contact-line">http://harukaze-petclinic.example</div>
    </div>
  </footer>
</main>
</body>
</html>
```